Business Card

We need some ideas for corporate business cards. I'm interested in a double sided card, with one side featuring our corporate logo, the other side with employee information.

Corporate colors, logo etc. available at www.brivalo.com

Industry/Entity Type

Business

Requirements
Must have
• The "Brivalo" logo with stylized "O"

Nice to have
• Preferred font is calibri

```html
<!DOCTYPE html>
<html lang="en">
<head>
<meta charset="utf-8">
<title>Brivalo Business Card</title>
<link rel="stylesheet" href="https://fonts.googleapis.com/css2?family=Montserrat:wght@500;600;700&display=swap">
<style>
  :root {
    --brand-blue: #466192;
    --brand-blue-dark: #3a5280;
    --card-white: #ffffff;
    --backdrop: #d4d4d4;
    --photo-tone-a: #b8a99a;
    --photo-tone-b: #3c4250;
  }
  * { margin: 0; padding: 0; box-sizing: border-box; }
  html, body { width: 1200px; height: 848px; overflow: hidden; }
  body {
    background: var(--backdrop);
    font-family: "Montserrat", Arial, sans-serif;
    position: relative;
  }
  .card {
    position: absolute;
    top: 240px;
    width: 234px;
    height: 362px;
    overflow: hidden;
    background: var(--card-white);
  }
  .card--front { left: 339px; }
  .card--back { left: 617px; }

  /* Front */
  .front-panel {
    position: absolute; left: 0; top: 0;
    width: 100%; height: 297px;
    background: var(--brand-blue);
  }
  .tagline {
    position: absolute; left: 22px; top: 20px;
    color: var(--card-white);
    font-weight: 700; font-size: 18.5px;
    line-height: 20.5px; letter-spacing: 0.6px;
  }
  .tagline span { display: block; }
  .icon-band {
    position: absolute; left: 0; width: 190px; height: 6px;
    background: linear-gradient(90deg, rgba(30,45,80,0.35), rgba(30,45,80,0));
    filter: blur(2px);
  }
  .icon-band--top { top: 104px; }
  .icon-band--bottom { top: 145px; }
  .service-icons {
    position: absolute; left: 22px; top: 118px;
  }
  .front-logo-area {
    position: absolute; left: 0; top: 297px;
    width: 100%; height: 65px;
    background: var(--card-white);
  }
  .wordmark {
    position: absolute; right: 22px; top: 20px;
    color: var(--brand-blue);
    font-weight: 700; font-size: 21px; letter-spacing: 2px;
  }

  /* Back */
  .photo {
    position: absolute; left: 11px; top: 18px;
    width: 69px; height: 72px;
    background: linear-gradient(180deg, var(--photo-tone-a), var(--photo-tone-b));
  }
  .person {
    position: absolute; left: 93px; top: 70px;
    color: var(--brand-blue);
    font-weight: 700; font-size: 8.4px; line-height: 12.5px;
  }
  .person-contact { margin-top: 13px; line-height: 13px; }
  .person-contact b, .office-contact b { font-weight: 700; }
  .person-contact span, .office-contact span { font-weight: 600; }
  .office-panel {
    position: absolute; left: 0; top: 179px;
    width: 100%; height: 183px;
    background: var(--brand-blue);
    color: var(--card-white);
    font-size: 8.4px; font-weight: 600; line-height: 12px;
    padding: 22px 0 0 22px;
  }
  .office-contact { margin-top: 13px; }
  .office-web { margin-top: 18px; font-weight: 700; }
</style>
</head>
<body>
  <section class="card card--front">
    <div class="front-panel">
      <h1 class="tagline"><span>INTELLIGENT</span><span>DIGITAL</span><span>SOLUTIONS</span></h1>
      <div class="icon-band icon-band--top"></div>
      <div class="icon-band icon-band--bottom"></div>
      <svg class="service-icons" width="100" height="40" viewBox="0 0 100 40" aria-hidden="true">
        <g fill="#fff">
          <g transform="translate(9,9)">
            <circle r="5.5"/>
            <rect x="-1.8" y="-8" width="3.6" height="16"/>
            <rect x="-8" y="-1.8" width="16" height="3.6"/>
            <rect x="-1.8" y="-8" width="3.6" height="16" transform="rotate(45)"/>
            <rect x="-1.8" y="-8" width="3.6" height="16" transform="rotate(-45)"/>
            <circle r="2.3" fill="#466192"/>
          </g>
          <g transform="translate(42,9)">
            <circle r="7.3" fill="none" stroke="#fff" stroke-width="1.6"/>
            <path d="M3.5 -3.5 L1 1 L-3.5 3.5 L-1 -1 Z"/>
          </g>
          <g transform="translate(75,9)">
            <path d="M-11 0 Q0 -10 11 0 Q0 10 -11 0 Z"/>
            <circle r="4" fill="#466192"/>
            <circle r="2" fill="#fff"/>
          </g>
        </g>
        <g stroke="rgba(255,255,255,0.45)" stroke-width="1">
          <line x1="9.5" y1="30" x2="9.5" y2="37"/>
          <line x1="42.5" y1="30" x2="42.5" y2="37"/>
          <line x1="75.5" y1="30" x2="75.5" y2="37"/>
        </g>
      </svg>
    </div>
    <div class="front-logo-area">
      <div class="wordmark">BRIVALO</div>
    </div>
  </section>

  <section class="card card--back">
    <div class="photo" role="img" aria-label="Portrait photo of the employee"></div>
    <div class="person">
      <div>JONH DOE</div>
      <div>EXECUTIVE DIRECTOR</div>
      <div class="person-contact">
        <div><b>TEL:</b> <span>(+353) 1 555 0142</span></div>
        <div><b>FAX:</b> <span>(+353) 1 555 0187</span></div>
        <div><span>JONH.DOE@BRIVALO.COM</span></div>
      </div>
    </div>
    <div class="office-panel">
      <address class="office-address" style="font-style:normal">
        <div>14 HARLOW LANE</div>
        <div>GREYFIELD BUSINESS PARK</div>
        <div>DUBLIN 9</div>
        <div>DUBLIN, DB</div>
      </address>
      <div class="office-contact">
        <div><b>TEL:</b> <span>(+353) 1 555 0142</span></div>
        <div><b>FAX:</b> <span>(+353) 1 555 0187</span></div>
        <div><span>INFO@BRIVALO.COM</span></div>
      </div>
      <div class="office-web">BRIVALO.COM</div>
    </div>
  </section>
</body>
</html>
```